Wholesale Vegetable Business Needs a Signboard Design!

We need a signboard design for a company based in Singapore, Tanjung Meriba Wholesale Centre. We are a wholesaler of fresh vegetables for numerous major customers. We would like to see designs that suits our logo which will be attached to this design brief. The final design should communicate reliability and growth. The signboard should have the logo (please rework logo as attachment is not of good quality) and company name as a 3D design with a pop-out feel but not too much, so as to remain relevant in the current market. Please refer to the attachment for a brief example of the 3D design mentioned. The company name shall be in English (top) as well as Mandarin (bottom). The English font is up to the designer, however the Mandarin font should be similar to the sample as per attached. The English company name is Wenhe Import Pte Ltd. The Mandarin company name is 文禾进口私人有限公司. Looking forward to your designs!
Updates

Hi, to answer some of the questions posed;

1) The dimensions are 470cm by 40cm.
2) Only the logo and text (both english and mandarin) is sufficient.
3) Frame or frameless designs are both fine.

Thank you.

Reason: Hi all, would like to see more designs. Thanks!

Reason: Hi all, would still like to see more creative designs. Thanks!

Target Market(s)

Caterers, retailers, import and export customers of fresh vegetables.

Industry/Entity Type

Business

Requirements
Must have
• Must have the attached logo (please rework it as attached logo is not of good quality), english company name, and mandarin company name.

```html
<!DOCTYPE html>
<html lang="en">
<head>
<meta charset="utf-8">
<title>Wenhe Import Pte Ltd — Signboard</title>
<link href="https://fonts.googleapis.com/css2?family=Jost:wght@700&family=Noto+Sans+SC:wght@400&display=swap" rel="stylesheet">
<style>
  :root {
    --board-green: #1d5a28;
    --board-edge: #174a20;
    --name-yellow: #f6d51f;
    --mark-lime: #a6d83a;
  }
  html, body {
    margin: 0;
    padding: 0;
    width: 1200px;
    height: 102px;
    overflow: hidden;
    background: var(--board-green);
  }
  .signboard {
    position: relative;
    width: 1200px;
    height: 102px;
    box-sizing: border-box;
    background: var(--board-green);
    border: 2px solid var(--board-edge);
  }
  .company-name {
    position: absolute;
    left: 0;
    right: 0;
    top: 0;
    text-align: center;
    color: var(--name-yellow);
    margin: 0;
  }
  .company-name__english {
    display: block;
    font-family: "Jost", "Futura", sans-serif;
    font-weight: 700;
    font-size: 41px;
    line-height: 1;
    letter-spacing: 2px;
    padding-top: 8px;
  }
  .company-name__mandarin {
    display: block;
    font-family: "Noto Sans SC", sans-serif;
    font-weight: 400;
    font-size: 28px;
    line-height: 1;
    letter-spacing: 3.5px;
    margin-top: 8px;
  }
  .brand-mark {
    position: absolute;
    top: 8px;
    width: 84px;
    display: flex;
    flex-direction: column;
    align-items: center;
  }
  .brand-mark--left { left: 4px; }
  .brand-mark--right { right: 4px; }
  .brand-mark__dot {
    width: 58px;
    height: 58px;
    border-radius: 50%;
    background: var(--mark-lime);
  }
  .brand-mark__name {
    margin-top: 6px;
    font-family: "Jost", "Futura", sans-serif;
    font-weight: 700;
    font-size: 15px;
    line-height: 1;
    letter-spacing: 1px;
    color: var(--name-yellow);
  }
</style>
</head>
<body>
  <div class="signboard">
    <div class="brand-mark brand-mark--left">
      <div class="brand-mark__dot"></div>
      <span class="brand-mark__name">WENHE</span>
    </div>

    <h1 class="company-name">
      <span class="company-name__english">Wenhe Import Pte Ltd</span>
      <span class="company-name__mandarin" lang="zh-Hans">文禾进口私人有限公司</span>
    </h1>

    <div class="brand-mark brand-mark--right">
      <div class="brand-mark__dot"></div>
      <span class="brand-mark__name">WENHE</span>
    </div>
  </div>
</body>
</html>
```